looking to design ads for a calendar.

We have the copy and brand assets created and ready to go. We need 1 large design for the front of the calendar and inside of the calendar. The specs are:

First interior page: 5 inches by 7.5 inches
Month pages (14 in total): 2.5 inches by 7.5 inches
PDF preferred, high resolution

```html
<!DOCTYPE html>
<html lang="en">
<head>
<meta charset="utf-8">
<title>2025 Counties in Focus Calendar</title>
<link href="https://fonts.googleapis.com/css2?family=Barlow:ital,wght@0,400;0,600;0,700;1,400;1,600&family=Roboto:wght@400;500;700;900&family=Roboto+Condensed:wght@400;500&display=swap" rel="stylesheet">
<style>
:root{
  --backdrop:#c6c7c9;
  --paper:#ffffff;
  --ink:#2b2b2b;
  --ink-soft:#6e6e6e;
  --rule:#3a3a3a;
  --header:#333333;
  --green:#2f6f5a;
  --gold:#e0b12c;
  --purple:#5b2d8e;
  --purple-deep:#3a2160;
  --purple-mist:#7d68a8;
  --sky:#5b9ed6;
  --sidebar-panel:#f1f1f3;
  --dot:#5e2b8c;
}
*{box-sizing:border-box;margin:0;padding:0}
html,body{width:1200px;height:744px;overflow:hidden}
body{background:var(--backdrop);position:relative;font-family:"Roboto",Arial,sans-serif;color:var(--ink)}
.page{position:absolute;top:169px;width:526px;height:406px;background:var(--paper)}
.page--overview{left:60px}
.page--january{left:614px}

/* association name */
.assoc{position:absolute;display:flex;align-items:center;gap:4px;font-family:"Roboto",Arial,sans-serif;font-weight:700;color:var(--green);white-space:nowrap;line-height:1}
.assoc__mark{width:6px;height:6px;background:var(--green);flex:none}
.page--overview .assoc{left:34px;top:52px;font-size:12px}
.page--january .assoc{left:12px;top:42px;font-size:11px}

/* mini calendars */
.mini{position:absolute;width:68px}
.mini h4{font-size:5.4px;font-weight:700;text-align:center;margin-bottom:1.5px;color:var(--ink)}
.mini h4 span{font-weight:400}
.mini .grid{display:grid;grid-template-columns:repeat(7,1fr);border:.6px solid var(--rule);border-top:none}
.mini .grid b{background:var(--header);color:#fff;font-size:3.6px;font-weight:700;text-align:center;height:6px;line-height:6px}
.mini .grid i{font-style:normal;font-size:3.8px;font-weight:500;text-align:center;height:8.4px;line-height:8.4px;border-right:.4px solid var(--rule);border-top:.4px solid var(--rule)}
.mini .grid i:nth-child(7n){border-right:none}
.mini .grid i.split{font-size:2.6px;letter-spacing:-.1px}
.c1{left:34px}.c2{left:112px}.c3{left:191px}
.r0{top:34px}.r1{top:106px}.r2{top:173px}.r3{top:248px}.r4{top:321px}
.mini--muted h4{color:var(--ink-soft);font-weight:400}
.mini--muted .grid{border-color:#9a9a9a}
.mini--muted .grid b{background:#8d8d8d}
.mini--muted .grid i{color:#555;border-color:#9a9a9a}

/* cover photo */
.cover-photo{position:absolute;left:271px;top:26px;width:243px;height:315px;background:linear-gradient(180deg,var(--sky) 0%,#8cc1ea 35%,#c79f5f 62%,#6c5438 100%)}
.cover-photo__tagline{position:absolute;left:0;right:0;top:40px;text-align:center;font-family:"Barlow",Arial,sans-serif;font-style:italic;font-weight:600;font-size:10.5px;line-height:14px;color:#2f2f33}

/* wordmark */
.wordmark{position:absolute;display:flex;align-items:center;gap:4px;font-family:"Roboto",Arial,sans-serif;font-weight:400;font-size:16px;line-height:1;color:var(--ink);white-space:nowrap}
.wordmark__mark{width:6px;height:6px;background:var(--green)}
.wordmark__by{position:absolute;right:0;top:19px;font-size:3.5px}
.page--overview .wordmark{left:432px;top:347px}
.page--january .wordmark{left:430px;top:356px}
.gold-bar{position:absolute;height:6px;background:var(--gold)}
.page--overview .gold-bar{left:426px;width:88px;top:386px}
.page--january .gold-bar{left:423px;width:97px;top:389px}
.page-dot{position:absolute;left:260px;top:392px;width:6px;height:6px;border-radius:50%;background:var(--dot)}

/* january header */
.month-kicker{position:absolute;left:92px;top:21px;font-size:17px;font-weight:700;color:#858585;white-space:nowrap}
.month-kicker em{font-family:"Barlow",Arial,sans-serif;font-weight:600;font-size:13.5px;color:#555}
.month-title{position:absolute;left:91px;top:42px;font-weight:900;font-size:29px;letter-spacing:.3px;line-height:1;color:var(--ink)}
.mini.prev{left:264px;top:26px}.mini.next{left:341px;top:26px}
.mini-divider{position:absolute;left:337px;top:28px;width:.6px;height:56px;background:#999}

/* month grid */
.month-grid{position:absolute;left:26px;top:95px;width:383px;border:.8px solid var(--rule)}
.month-grid__days{display:grid;grid-template-columns:repeat(7,1fr);background:var(--header);color:#fff;font-family:"Roboto Condensed",Arial,sans-serif;font-size:7.4px;font-weight:400;text-align:center;height:12px;line-height:12px}
.month-grid__cells{display:grid;grid-template-columns:repeat(7,1fr);grid-auto-rows:57.6px}
.month-grid__cells div{border-right:.8px solid var(--rule);border-bottom:.8px solid var(--rule)}
.month-grid__cells div:nth-child(7n){border-right:none}
.month-grid__cells div:nth-last-child(-n+7){border-bottom:none}

/* sidebar */
.sidebar{position:absolute;left:423px;top:30px;width:97px;height:308px;background:var(--sidebar-panel);overflow:hidden}
.sidebar__photo{position:absolute;left:0;top:0;width:97px;height:140px;background:linear-gradient(160deg,var(--purple-mist) 0%,var(--purple-deep) 60%,#2a1a45 100%)}
.sidebar__milestone{position:absolute;left:0;right:0;top:48px;text-align:center;color:#fff}
.sidebar__year{font-weight:900;font-size:11.5px;line-height:12.5px}
.sidebar__event{font-family:"Barlow",Arial,sans-serif;font-style:italic;font-size:9.5px;margin-top:5px}
.sidebar__bands{position:absolute;left:0;width:97px}
.sidebar__copy{position:absolute;left:5px;right:5px;top:168px;text-align:center;font-family:"Barlow",Arial,sans-serif;font-style:italic;font-size:7.2px;line-height:14.6px;color:#2d2d2d}
</style>
</head>
<body>

<section class="page page--overview">
  <div class="assoc"><span class="assoc__mark"></span>ECA United</div>

  <div class="mini c2 r0"><h4>November <span>2024</span></h4><div class="grid"><b>S</b><b>M</b><b>T</b><b>W</b><b>T</b><b>F</b><b>S</b><i></i><i></i><i></i><i></i><i></i><i>1</i><i>2</i><i>3</i><i>4</i><i>5</i><i>6</i><i>7</i><i>8</i><i>9</i><i>10</i><i>11</i><i>12</i><i>13</i><i>14</i><i>15</i><i>16</i><i>17</i><i>18</i><i>19</i><i>20</i><i>21</i><i>22</i><i>23</i><i>24</i><i>25</i><i>26</i><i>27</i><i>28</i><i>29</i><i>30</i></div></div>
  <div class="mini c3 r0"><h4>December <span>2024</span></h4><div class="grid"><b>S</b><b>M</b><b>T</b><b>W</b><b>T</b><b>F</b><b>S</b><i>1</i><i>2</i><i>3</i><i>4</i><i>5</i><i>6</i><i>7</i><i>8</i><i>9</i><i>10</i><i>11</i><i>12</i><i>13</i><i>14</i><i>15</i><i>16</i><i>17</i><i>18</i><i>19</i><i>20</i><i>21</i><i>22</i><i>23</i><i>24</i><i>25</i><i>26</i><i>27</i><i>28</i><i>29</i><i>30</i><i>31</i><i></i><i></i><i></i><i></i></div></div>

  <div class="mini c1 r1"><h4>January <span>2025</span></h4><div class="grid"><b>S</b><b>M</b><b>T</b><b>W</b><b>T</b><b>F</b><b>S</b><i></i><i></i><i></i><i>1</i><i>2</i><i>3</i><i>4</i><i>5</i><i>6</i><i>7</i><i>8</i><i>9</i><i>10</i><i>11</i><i>12</i><i>13</i><i>14</i><i>15</i><i>16</i><i>17</i><i>18</i><i>19</i><i>20</i><i>21</i><i>22</i><i>23</i><i>24</i><i>25</i><i>26</i><i>27</i><i>28</i><i>29</i><i>30</i><i>31</i><i></i></div></div>
  <div class="mini c2 r1"><h4>February <span>2025</span></h4><div class="grid"><b>S</b><b>M</b><b>T</b><b>W</b><b>T</b><b>F</b><b>S</b><i></i><i></i><i></i><i></i><i></i><i></i><i>1</i><i>2</i><i>3</i><i>4</i><i>5</i><i>6</i><i>7</i><i>8</i><i>9</i><i>10</i><i>11</i><i>12</i><i>13</i><i>14</i><i>15</i><i>16</i><i>17</i><i>18</i><i>19</i><i>20</i><i>21</i><i>22</i><i>23</i><i>24</i><i>25</i><i>26</i><i>27</i><i>28</i><i></i></div></div>
  <div class="mini c3 r1"><h4>March <span>2025</span></h4><div class="grid"><b>S</b><b>M</b><b>T</b><b>W</b><b>T</b><b>F</b><b>S</b><i></i><i></i><i></i><i></i><i></i><i></i><i>1</i><i>2</i><i>3</i><i>4</i><i>5</i><i>6</i><i>7</i><i>8</i><i>9</i><i>10</i><i>11</i><i>12</i><i>13</i><i>14</i><i>15</i><i>16</i><i>17</i><i>18</i><i>19</i><i>20</i><i>21</i><i>22</i><i class="split">23/30</i><i class="split">24/31</i><i>25</i><i>26</i><i>27</i><i>28</i><i>29</i></div></div>

  <div class="mini c1 r2"><h4>April <span>2025</span></h4><div class="grid"><b>S</b><b>M</b><b>T</b><b>W</b><b>T</b><b>F</b><b>S</b><i></i><i></i><i>1</i><i>2</i><i>3</i><i>4</i><i>5</i><i>6</i><i>7</i><i>8</i><i>9</i><i>10</i><i>11</i><i>12</i><i>13</i><i>14</i><i>15</i><i>16</i><i>17</i><i>18</i><i>19</i><i>20</i><i>21</i><i>22</i><i>23</i><i>24</i><i>25</i><i>26</i><i>27</i><i>28</i><i>29</i><i>30</i><i></i><i></i><i></i></div></div>
  <div class="mini c2 r2"><h4>May <span>2025</span></h4><div class="grid"><b>S</b><b>M</b><b>T</b><b>W</b><b>T</b><b>F</b><b>S</b><i></i><i></i><i></i><i></i><i>1</i><i>2</i><i>3</i><i>4</i><i>5</i><i>6</i><i>7</i><i>8</i><i>9</i><i>10</i><i>11</i><i>12</i><i>13</i><i>14</i><i>15</i><i>16</i><i>17</i><i>18</i><i>19</i><i>20</i><i>21</i><i>22</i><i>23</i><i>24</i><i>25</i><i>26</i><i>27</i><i>28</i><i>29</i><i>30</i><i>31</i></div></div>
  <div class="mini c3 r2"><h4>June <span>2025</span></h4><div class="grid"><b>S</b><b>M</b><b>T</b><b>W</b><b>T</b><b>F</b><b>S</b><i>1</i><i>2</i><i>3</i><i>4</i><i>5</i><i>6</i><i>7</i><i>8</i><i>9</i><i>10</i><i>11</i><i>12</i><i>13</i><i>14</i><i>15</i><i>16</i><i>17</i><i>18</i><i>19</i><i>20</i><i>21</i><i>22</i><i>23</i><i>24</i><i>25</i><i>26</i><i>27</i><i>28</i><i>29</i><i>30</i><i></i><i></i><i></i><i></i><i></i></div></div>

  <div class="mini c1 r3"><h4>July <span>2025</span></h4><div class="grid"><b>S</b><b>M</b><b>T</b><b>W</b><b>T</b><b>F</b><b>S</b><i></i><i></i><i>1</i><i>2</i><i>3</i><i>4</i><i>5</i><i>6</i><i>7</i><i>8</i><i>9</i><i>10</i><i>11</i><i>12</i><i>13</i><i>14</i><i>15</i><i>16</i><i>17</i><i>18</i><i>19</i><i>20</i><i>21</i><i>22</i><i>23</i><i>24</i><i>25</i><i>26</i><i>27</i><i>28</i><i>29</i><i>30</i><i>31</i><i></i><i></i></div></div>
  <div class="mini c2 r3"><h4>August <span>2025</span></h4><div class="grid"><b>S</b><b>M</b><b>T</b><b>W</b><b>T</b><b>F</b><b>S</b><i></i><i></i><i></i><i></i><i></i><i>1</i><i>2</i><i>3</i><i>4</i><i>5</i><i>6</i><i>7</i><i>8</i><i>9</i><i>10</i><i>11</i><i>12</i><i>13</i><i>14</i><i>15</i><i>16</i><i>17</i><i>18</i><i>19</i><i>20</i><i>21</i><i>22</i><i>23</i><i class="split">24/31</i><i>25</i><i>26</i><i>27</i><i>28</i><i>29</i><i>30</i></div></div>
  <div class="mini c3 r3"><h4>September <span>2025</span></h4><div class="grid"><b>S</b><b>M</b><b>T</b><b>W</b><b>T</b><b>F</b><b>S</b><i></i><i>1</i><i>2</i><i>3</i><i>4</i><i>5</i><i>6</i><i>7</i><i>8</i><i>9</i><i>10</i><i>11</i><i>12</i><i>13</i><i>14</i><i>15</i><i>16</i><i>17</i><i>18</i><i>19</i><i>20</i><i>21</i><i>22</i><i>23</i><i>24</i><i>25</i><i>26</i><i>27</i><i>28</i><i>29</i><i>30</i><i></i><i></i><i></i><i></i></div></div>

  <div class="mini c1 r4"><h4>October <span>2025</span></h4><div class="grid"><b>S</b><b>M</b><b>T</b><b>W</b><b>T</b><b>F</b><b>S</b><i></i><i></i><i></i><i>1</i><i>2</i><i>3</i><i>4</i><i>5</i><i>6</i><i>7</i><i>8</i><i>9</i><i>10</i><i>11</i><i>12</i><i>13</i><i>14</i><i>15</i><i>16</i><i>17</i><i>18</i><i>19</i><i>20</i><i>21</i><i>22</i><i>23</i><i>24</i><i>25</i><i>26</i><i>27</i><i>28</i><i>29</i><i>30</i><i>31</i><i></i></div></div>
  <div class="mini c2 r4"><h4>November <span>2025</span></h4><div class="grid"><b>S</b><b>M</b><b>T</b><b>W</b><b>T</b><b>F</b><b>S</b><i></i><i></i><i></i><i></i><i></i><i></i><i>1</i><i>2</i><i>3</i><i>4</i><i>5</i><i>6</i><i>7</i><i>8</i><i>9</i><i>10</i><i>11</i><i>12</i><i>13</i><i>14</i><i>15</i><i>16</i><i>17</i><i>18</i><i>19</i><i>20</i><i>21</i><i>22</i><i class="split">23/30</i><i>24</i><i>25</i><i>26</i><i>27</i><i>28</i><i>29</i></div></div>
  <div class="mini c3 r4"><h4>December <span>2025</span></h4><div class="grid"><b>S</b><b>M</b><b>T</b><b>W</b><b>T</b><b>F</b><b>S</b><i></i><i>1</i><i>2</i><i>3</i><i>4</i><i>5</i><i>6</i><i>7</i><i>8</i><i>9</i><i>10</i><i>11</i><i>12</i><i>13</i><i>14</i><i>15</i><i>16</i><i>17</i><i>18</i><i>19</i><i>20</i><i>21</i><i>22</i><i>23</i><i>24</i><i>25</i><i>26</i><i>27</i><i>28</i><i>29</i><i>30</i><i>31</i><i></i><i></i><i></i></div></div>

  <div class="cover-photo" role="img" aria-label="Upward view of city office towers against a clear blue sky">
    <p class="cover-photo__tagline">A Century of Stewardship.<br>A Future of Financial Strength.</p>
  </div>

  <div class="wordmark"><span class="wordmark__mark"></span>Ledgerwise<span class="wordmark__by">by Northpoint</span></div>
  <div class="gold-bar"></div>
  <div class="page-dot"></div>
</section>

<section class="page page--january">
  <div class="assoc"><span class="assoc__mark"></span>ECA United</div>
  <p class="month-kicker">2025 <em>Counties in Focus</em></p>
  <h1 class="month-title">JANUARY</h1>

  <div class="mini mini--muted prev"><h4>December 2024</h4><div class="grid"><b>S</b><b>M</b><b>T</b><b>W</b><b>T</b><b>F</b><b>S</b><i>1</i><i>2</i><i>3</i><i>4</i><i>5</i><i>6</i><i>7</i><i>8</i><i>9</i><i>10</i><i>11</i><i>12</i><i>13</i><i>14</i><i>15</i><i>16</i><i>17</i><i>18</i><i>19</i><i>20</i><i>21</i><i>22</i><i>23</i><i>24</i><i>25</i><i>26</i><i>27</i><i>28</i><i>29</i><i>30</i><i>31</i><i></i><i></i><i></i><i></i></div></div>
  <div class="mini-divider"></div>
  <div class="mini mini--muted next"><h4>February 2025</h4><div class="grid"><b>S</b><b>M</b><b>T</b><b>W</b><b>T</b><b>F</b><b>S</b><i></i><i></i><i></i><i></i><i></i><i></i><i>1</i><i>2</i><i>3</i><i>4</i><i>5</i><i>6</i><i>7</i><i>8</i><i>9</i><i>10</i><i>11</i><i>12</i><i>13</i><i>14</i><i>15</i><i>16</i><i>17</i><i>18</i><i>19</i><i>20</i><i>21</i><i>22</i><i>23</i><i>24</i><i>25</i><i>26</i><i>27</i><i>28</i><i></i></div></div>

  <div class="month-grid">
    <div class="month-grid__days"><span>SUNDAY</span><span>MONDAY</span><span>TUESDAY</span><span>WEDNESDAY</span><span>THURSDAY</span><span>FRIDAY</span><span>SATURDAY</span></div>
    <div class="month-grid__cells">
      <div></div><div></div><div></div><div></div><div></div><div></div><div></div>
      <div></div><div></div><div></div><div></div><div></div><div></div><div></div>
      <div></div><div></div><div></div><div></div><div></div><div></div><div></div>
      <div></div><div></div><div></div><div></div><div></div><div></div><div></div>
      <div></div><div></div><div></div><div></div><div></div><div></div><div></div>
    </div>
  </div>

  <aside class="sidebar">
    <div class="sidebar__photo" role="img" aria-label="Purple-toned photo of a team working together at a desk">
      <div class="sidebar__milestone">
        <p class="sidebar__year">JANUARY<br>1925:</p>
        <p class="sidebar__event">ECA is born.</p>
      </div>
    </div>
    <svg class="sidebar__bands" style="top:124px" width="97" height="32" viewBox="0 0 96 32" aria-hidden="true">
      <polygon points="0,8 30,2 60,10 96,4 96,32 70,22 48,18 24,22 0,18" fill="#8a5bbd"/>
      <polygon points="0,18 24,22 48,18 70,22 96,16 96,26 48,22 0,30" fill="#5b2d8e"/>
    </svg>
    <p class="sidebar__copy">For 100 years, ECA has empowered counties to lead with purpose. Today, Ledgerwise helps your finance team lead with precision, using data to drive every treasury decision.</p>
    <svg class="sidebar__bands" style="top:292px" width="97" height="16" viewBox="0 0 96 16" aria-hidden="true">
      <polygon points="0,0 30,8 56,2 96,6 96,16 0,16" fill="#8a5bbd"/>
      <polygon points="0,6 40,12 96,4 96,16 0,16" fill="#5b2d8e"/>
    </svg>
  </aside>

  <div class="wordmark"><span class="wordmark__mark"></span>Ledgerwise<span class="wordmark__by">by Northpoint</span></div>
  <div class="gold-bar"></div>
  <div class="page-dot"></div>
</section>

</body>
</html>
```